Tallbrook Meridian Advisory needs business cards

Tallbrook Meridian Advisory is a new approach to consulting: we believe in partnering our clients in a hands-on, side-by-side, rolling-up-our sleeves approach, rather than being removed and aloof consultants.

We have a logo design developped through PixelHarbor (see attachment) and need to move to the stage of designing a business card for our 7 founding members.

Target Market(s)

Senior executives in local and global companies (such as Fizzmont Tonic, Hollanby, Brevard, etc)

Industry/Entity Type

Business

Requirements
Must have
• Look and feel: The design reflect the logo: i.e. professional, modern and approachable (as opposed to corporate traditional and remote). We are looking for a high quality, premium design.

Content must haves:
- prominent: our logo, person's name, function, phone number and e-mail address
- less prominent: company address and website

Example: Tallbrook Meridian Advisory logo, Mireille Vostag, Partner, +44 (0)781 209 3375, mireille_vostag@tallbrookmeridian.example / 17 Pelham Crescent, Esher, Surrey, UK, KT10 3WN - www.tallbrookmeridian.example

- Both sides of the card can be used
- Both versions of the logo can be used (on black or on white)

```html
<!DOCTYPE html>
<html lang="en">
<head>
<meta charset="utf-8">
<title>Tallbrook Meridian Advisory — Business Cards</title>
<link rel="stylesheet" href="https://fonts.googleapis.com/css2?family=Source+Sans+3:wght@400;600;700&display=swap">
<style>
  :root {
    --page-bg: #ffffff;
    --navy: #0b3f7a;
    --blue-deep: #0d4a8c;
    --blue-mid: #1a66ad;
    --blue-bright: #2f8fd8;
    --blue-name: #1577c7;
    --ink: #333333;
    --rule: #6e6e6e;
    --white: #ffffff;
    --card-shadow: 0 6px 10px rgba(0, 0, 0, 0.35);
  }
  * { box-sizing: border-box; margin: 0; padding: 0; }
  html, body {
    width: 1200px;
    height: 900px;
    overflow: hidden;
    background: var(--page-bg);
    font-family: "Source Sans 3", "Myriad Pro", Arial, sans-serif;
  }
  .canvas { position: relative; width: 1200px; height: 900px; }

  .card {
    position: absolute;
    left: 287px;
    width: 658px;
    height: 378px;
    box-shadow: var(--card-shadow);
    overflow: hidden;
  }
  .card__art { position: absolute; left: 0; top: 0; }

  /* Front */
  .card--front {
    top: 48px;
    background: radial-gradient(ellipse 70% 90% at 42% 50%, var(--blue-mid) 0%, var(--blue-deep) 55%, var(--navy) 100%);
  }
  .brand { position: absolute; display: flex; align-items: center; }
  .brand__dot { border-radius: 50%; flex: none; }
  .brand__name { font-weight: 600; line-height: 1.05; letter-spacing: -0.3px; }
  .card--front .brand { left: 153px; top: 129px; }
  .card--front .brand__dot { width: 132px; height: 132px; background: var(--blue-bright); margin-right: 14px; }
  .card--front .brand__name { color: var(--white); font-size: 34px; }

  /* Back */
  .card--back { top: 485px; background: var(--white); }
  .card--back .brand { left: 293px; top: 26px; }
  .card--back .brand__dot { width: 108px; height: 108px; background: var(--blue-bright); margin-right: 12px; }
  .card--back .brand__name { color: var(--ink); font-size: 27px; }

  .contact { position: absolute; left: 47px; top: 170px; width: 300px; }
  .contact__name { color: var(--blue-name); font-weight: 700; font-size: 21px; line-height: 1; }
  .contact__role { color: var(--ink); font-size: 16px; margin-top: 5px; line-height: 1; }
  .contact__rule { height: 2px; background: var(--rule); margin-top: 9px; width: 288px; }
  .contact__list { list-style: none; margin-top: 7px; }
  .contact__item {
    display: flex; align-items: center; gap: 6px;
    color: var(--ink); font-size: 16px; line-height: 24px; white-space: nowrap;
  }
  .contact__icon { width: 13px; height: 13px; flex: none; display: block; }

  .footer {
    position: absolute; left: 47px; right: 30px; top: 338px;
    display: flex; gap: 26px;
    color: var(--white); font-size: 15px; white-space: nowrap;
  }
</style>
</head>
<body>
<main class="canvas">

  <section class="card card--front" aria-label="Card front">
    <div class="brand">
      <span class="brand__dot"></span>
      <span class="brand__name">Tallbrook Meridian<br>Advisory</span>
    </div>
  </section>

  <section class="card card--back" aria-label="Card back">
    <svg class="card__art" width="658" height="378" viewBox="0 0 658 378" aria-hidden="true">
      <defs>
        <linearGradient id="band" x1="0" y1="0" x2="1" y2="0">
          <stop offset="0" stop-color="#0b3f7a"/>
          <stop offset="0.6" stop-color="#1a5fa6"/>
          <stop offset="1" stop-color="#0d4a8c"/>
        </linearGradient>
        <linearGradient id="swoosh" x1="0" y1="0" x2="1" y2="0">
          <stop offset="0" stop-color="#f0f0f0"/>
          <stop offset="0.4" stop-color="#9a9a9a"/>
          <stop offset="1" stop-color="#cfcfcf"/>
        </linearGradient>
      </defs>
      <path d="M0,292 C200,302 460,282 658,214 L658,228 C460,288 220,306 0,326 Z" fill="url(#swoosh)"/>
      <path d="M0,326 C220,306 460,288 658,228 L658,378 L0,378 Z" fill="url(#band)"/>
    </svg>

    <div class="brand">
      <span class="brand__dot"></span>
      <span class="brand__name">Tallbrook Meridian<br>Advisory</span>
    </div>

    <div class="contact">
      <p class="contact__name">Mireille Vostag</p>
      <p class="contact__role">Partner</p>
      <div class="contact__rule"></div>
      <ul class="contact__list">
        <li class="contact__item">
          <svg class="contact__icon" width="13" height="13" viewBox="0 0 24 24" aria-hidden="true"><path fill="#1577c7" d="M6.6 10.8a15.1 15.1 0 0 0 6.6 6.6l2.2-2.2a1 1 0 0 1 1-.25 11.4 11.4 0 0 0 3.6.57 1 1 0 0 1 1 1V20a1 1 0 0 1-1 1A17 17 0 0 1 3 4a1 1 0 0 1 1-1h3.5a1 1 0 0 1 1 1c0 1.25.2 2.45.57 3.57a1 1 0 0 1-.25 1z"/></svg>
          <span>+44 (0)781 209 3375</span>
        </li>
        <li class="contact__item">
          <svg class="contact__icon" width="13" height="13" viewBox="0 0 24 24" aria-hidden="true"><rect x="1" y="5" width="22" height="14" fill="#1577c7"/><path d="M1 5l11 8 11-8" fill="none" stroke="#ffffff" stroke-width="1.8"/></svg>
          <span>mireille_vostag@tallbrookmeridian.example</span>
        </li>
      </ul>
    </div>

    <p class="footer">
      <span>17 Pelham Crescent, Esher, Surrey, UK, KT10 3WN</span>
      <span>www.tallbrookmeridian.example</span>
    </p>
  </section>

</main>
</body>
</html>
```